Business Card Design for digital storytelling business

I need a business card for a workshop/consulting/coaching business.

Company Name: Bright Harbor Works

Tagline: Modern tools for timeless stories

What we do: Through workshops, webinars, and coaching we teach you how to capture, tell and share your important memories and stories using readily available digital tools. We will help you tell your life story in a format to share with your family now and in the future.
Updates

I just received a toll free number that I would like included on the designs. If the addition of a phone number would significantly alter your design, please submit an altered version. The number is 866-217-9086

Target Market(s)

Adults in US between ages of 35-70 interested in capturing, preserving and sharing memories and life stories in a digital format.
Could include the following:

-People touched by illness or tragedy who need to tell their own or a loved one's life story
-Grandparents wanting to share stories and wisdom with grandchildren living far away
-People with aging parents who want to capture their stories in a format to pass on to their children
-Alzheimer's patients and their families
-People wanting to transfer analog photos to digital; or wanting to organize digital photos into something that tells a story

Industry/Entity Type

Digital

Requirements
Must have
• Must include business name, logo, tagline

Contact information (see file)
Social media information

Fonts easily readable by aging eyes. Good contrast.

Nice to have
• Color preferences: blue, green, yellow/gold
Blue denotes the calm, non-pressured way that I teach. It is for the healing that comes from telling your story. It represents time and space that are bridged in the digital environment.
Green is for growth, the future, the family tree, Vines that grow and branch and connect the generations and our hearts.
Yellow/gold is for the legacy of wisdom in our lives and stories. It is for the light of truth we bring to the world by sharing our stories.
Should not have
• No old-style, script fonts.
No Times New Roman

```html
<!DOCTYPE html>
<html lang="en">
<head>
<meta charset="utf-8">
<title>Bright Harbor Works – Business Card</title>
<link rel="stylesheet" href="https://fonts.googleapis.com/css2?family=Open+Sans:wght@400;600&family=Marcellus&family=Michroma&display=swap">
<style>
  :root {
    --backdrop: #8a8d8f;
    --navy: #2f4068;
    --cream: #efd9a8;
    --green: #21994a;
    --white: #ffffff;
    --ink: #2f4068;
  }
  html, body {
    margin: 0;
    padding: 0;
    width: 1200px;
    height: 771px;
    overflow: hidden;
    background: var(--backdrop);
  }
  .canvas {
    position: relative;
    width: 1200px;
    height: 771px;
  }
  .card {
    position: absolute;
    top: 237px;
    width: 520px;
    height: 297px;
    overflow: hidden;
    box-shadow: 0 6px 18px rgba(0,0,0,0.25);
  }
  .card--front {
    left: 60px;
    background: var(--navy);
  }
  .card--back {
    left: 620px;
    background: var(--cream);
  }
  .card-bg {
    position: absolute;
    inset: 0;
  }

  /* Front side */
  .front-brand {
    position: absolute;
    left: 58px;
    top: 118px;
    color: var(--white);
  }
  .front-brand .brand-name {
    font-family: "Open Sans", sans-serif;
    font-weight: 400;
    font-size: 32px;
    line-height: 1;
    letter-spacing: 0.2px;
    white-space: nowrap;
  }
  .front-brand .tagline {
    margin-top: 8px;
    font-family: "Marcellus", serif;
    font-size: 12.5px;
    letter-spacing: 0.4px;
    text-transform: uppercase;
    white-space: nowrap;
  }

  /* Back side */
  .back-brand {
    position: absolute;
    right: 30px;
    top: 40px;
    text-align: right;
    color: var(--ink);
  }
  .back-brand .brand-row {
    display: flex;
    align-items: center;
    justify-content: flex-end;
    gap: 10px;
  }
  .brand-mark {
    width: 16px;
    height: 16px;
    background: var(--green);
  }
  .back-brand .brand-name {
    font-family: "Open Sans", sans-serif;
    font-weight: 400;
    font-size: 28px;
    line-height: 1;
    white-space: nowrap;
  }
  .back-brand .tagline {
    margin-top: 6px;
    font-family: "Marcellus", serif;
    font-size: 10.5px;
    letter-spacing: 0.3px;
    text-transform: uppercase;
    white-space: nowrap;
  }

  .identity {
    position: absolute;
    right: 282px;
    top: 194px;
    text-align: right;
    color: var(--white);
    font-family: "Michroma", sans-serif;
  }
  .identity .person-name {
    font-size: 10px;
    letter-spacing: 1px;
    text-transform: uppercase;
  }
  .identity .person-role {
    margin-top: 4px;
    font-size: 7.5px;
    letter-spacing: 0.6px;
  }
  .identity .address {
    margin-top: 16px;
    font-size: 7.5px;
    line-height: 16px;
    letter-spacing: 0.6px;
    text-transform: uppercase;
  }
  .divider {
    position: absolute;
    left: 250px;
    top: 192px;
    width: 1px;
    height: 88px;
    background: var(--white);
  }
  .contact-list {
    position: absolute;
    left: 262px;
    top: 194px;
    margin: 0;
    padding: 0;
    list-style: none;
    color: var(--white);
    font-family: "Michroma", sans-serif;
    font-size: 8.5px;
    letter-spacing: 0.6px;
  }
  .contact-list li {
    display: flex;
    align-items: center;
    gap: 6px;
    height: 17px;
    white-space: nowrap;
  }
  .contact-list .email,
  .contact-list .web {
    text-transform: uppercase;
  }
  .icon {
    width: 11px;
    height: 11px;
    flex: none;
  }
</style>
</head>
<body>
<main class="canvas">

  <section class="card card--front" aria-label="Business card front">
    <div class="front-brand">
      <div class="brand-name">Bright Harbor Works</div>
      <div class="tagline">Modern tools for timeless stories</div>
    </div>
  </section>

  <section class="card card--back" aria-label="Business card back">
    <svg class="card-bg" width="520" height="297" viewBox="0 0 520 297" aria-hidden="true">
      <path d="M0,54 C175,52 340,122 520,244 L520,262 C330,140 170,70 0,70 Z" fill="var(--green)"/>
      <path d="M0,70 C170,70 330,140 520,262 L520,297 L0,297 Z" fill="var(--navy)"/>
    </svg>

    <div class="back-brand">
      <div class="brand-row">
        <span class="brand-mark"></span>
        <span class="brand-name">Bright Harbor Works</span>
      </div>
      <div class="tagline">Modern tools for timeless stories</div>
    </div>

    <div class="identity">
      <div class="person-name">Daniel Reyes</div>
      <div class="person-role">Owner / C.E.O</div>
      <div class="address">Suite 18, Pier Bldg,<br>MA 02110</div>
    </div>

    <div class="divider"></div>

    <ul class="contact-list">
      <li>
        <svg class="icon" viewBox="0 0 12 12" aria-hidden="true"><circle cx="6" cy="6" r="6" fill="var(--white)"/><path d="M3.6,3 L5,3 L5.4,4.6 L4.6,5.2 C5,6.1 5.8,6.9 6.8,7.4 L7.4,6.6 L9,7 L9,8.4 C6,8.6 3.4,6 3.6,3 Z" fill="var(--navy)"/></svg>
        <span class="phone">866-217-9086</span>
      </li>
      <li>
        <svg class="icon" viewBox="0 0 12 12" aria-hidden="true"><circle cx="6" cy="6" r="6" fill="var(--white)"/><path d="M3.6,3 L5,3 L5.4,4.6 L4.6,5.2 C5,6.1 5.8,6.9 6.8,7.4 L7.4,6.6 L9,7 L9,8.4 C6,8.6 3.4,6 3.6,3 Z" fill="var(--navy)"/></svg>
        <span class="phone">617-555-0142</span>
      </li>
      <li>
        <svg class="icon" viewBox="0 0 12 12" aria-hidden="true"><circle cx="6" cy="6" r="6" fill="var(--white)"/><rect x="4.2" y="2.6" width="3.6" height="6.8" rx="0.6" fill="var(--navy)"/><rect x="4.8" y="3.4" width="2.4" height="4.4" fill="var(--white)"/></svg>
        <span class="phone">617-555-0187</span>
      </li>
      <li>
        <svg class="icon" viewBox="0 0 12 12" aria-hidden="true"><circle cx="6" cy="6" r="6" fill="var(--white)"/><rect x="3" y="4" width="6" height="4.2" fill="var(--navy)"/><path d="M3,4 L6,6.4 L9,4" fill="none" stroke="var(--white)" stroke-width="0.7"/></svg>
        <span class="email">hello@bhworks.com</span>
      </li>
      <li>
        <svg class="icon" viewBox="0 0 12 12" aria-hidden="true"><circle cx="6" cy="6" r="6" fill="var(--white)"/><circle cx="6" cy="6" r="3.2" fill="none" stroke="var(--navy)" stroke-width="0.8"/><path d="M2.8,6 L9.2,6 M6,2.8 C4.4,4.6 4.4,7.4 6,9.2 M6,2.8 C7.6,4.6 7.6,7.4 6,9.2" fill="none" stroke="var(--navy)" stroke-width="0.6"/></svg>
        <span class="web">www.bhworks.com</span>
      </li>
    </ul>
  </section>

</main>
</body>
</html>
```